Stylish Design With Simple UI For Appointment Site

Note: Logo file now attached. Extra credit to anyone who offers basic HTML templates in the final deliverable, incorporating the individual components of the design (using DIVs and CSS).

There are two key requirements for this site:

1. It makes our site look like one of the most professional of its kind. We want to look the part;
2. It has a very simple, straight-forward user interface. We're nothing without being intuitive.

Our site will be used by other businesses to set up their own online booking systems.

Logo samples attached. The colour scheme is not yet set but two possible options are:

1. Dark (#323B3A) & Blue (#12B5D4) on White background
2. White & Yellow (#FEF102) on Grey (#3A3A3C) background

For inspiration, and an idea of what we like, take a look at quillbarn.com - it's very clear and eye-catching, although its pages are longer than we would like ours to be. Oh but we don't need a chimp! Instead of the section with the chimp in, we would like a changing image headline section on the home page, in the style of fellgarde.co.uk (with a less high image; we have attached one image which you may want to try out with this, but happy to see other ideas).

Any graphics included must be royalty free and free for commercial use. Fonts should be readily available and specified.

We would like to see the design applied to the following pages:

1. The main public home page (features header, login prompt, menu, changing image banner with headlines, main body, footer menu).
2. A secondary public page (features a similar layout to home page but without image headline banner, includes extra panels/body detail).
3. The Control Panel page (features several list panels and an add appointment button).
4. A list-style administration page (with popup item editor window).
5. A settings administration page (with form).

In that order, a sample walk-through design spec will be attached.

To summarise, we are looking for someone to put forward not only a design but something which also focuses on the user interface. The designer should consider all of the examples and guidance given, but shouldn't let that limit any innovation.

Happy to respond to any questions and give constant feedback.

Thank you.

-*-*-*-*-*-*-*-*-*-*-*-*-*-*-*-*-

Update, 18th Nov 2011:

1. I'm about the upload the logos so you can incorporate these into your designs.

2. A UI question of mine is how to move from a list view (e.g. Resources) to editing one of those items in the list. In the spec document I showed a popup editor for these items but I don't know if that's the best thing to do. Happy to see other ideas on this - whatever the best user experience would be.

3. On the designs in the spec document I've not included any help functionality. It would be good to include pieces of guidance on each page of the administration area to help the user - guess these could either be info panels on the pages themselves or info popups. Again, would be good to see some ideas in the designs.

Also, just to be clear, I am really looking for something that looks like a modern innovative "web app" rather than it looking like a promotional corporate web site.

Target Market(s)

Owners of businesses of all types (e.g. salons, small hotels, surgeries, etc).

Industry/Entity Type

Commercial

Requirements
Must have
• Headline image transition panel on home page.

Layout, graphic and font styles along similar lines to quillbarn.com, fellgarde.co.uk, etc.
Nice to have
• Blog feed panel on the home page.

Innovative ideas for improvements to the spec.
Should not have
• Anything which can't be practically rendered when the design is converted to HTML.

Should not be overly influenced by the layout and style in the attached spec - that should just be a guide to the content and layout of the site.

```html
<!DOCTYPE html>
<html lang="en">
<head>
<meta charset="utf-8">
<title>Slotwise – Online booking for every business</title>
<link href="https://fonts.googleapis.com/css2?family=Open+Sans:ital,wght@0,400;0,600;0,700;1,400&family=Oswald:wght@500&display=swap" rel="stylesheet">
<style>
:root{
  --page:#f4f4f4;
  --ink:#3a3a3a;
  --dark:#2f2f31;
  --panel:#3a3a3c;
  --panel-deep:#2b2b2d;
  --blue:#12b5d4;
  --teal:#1f8ba3;
  --white:#ffffff;
  --muted:#cfcfcf;
}
*{box-sizing:border-box;margin:0;padding:0}
html,body{width:1200px;height:1118px;overflow:hidden}
body{background:var(--page);font-family:"Open Sans",Arial,sans-serif;color:var(--ink);position:relative}
a{color:inherit;text-decoration:none}

.top-strip{position:absolute;left:0;top:0;width:1200px;height:8px;background:var(--dark)}
.account-tab{position:absolute;left:882px;top:0;width:270px;height:50px;background:var(--panel);border-radius:0 0 8px 8px;display:flex;align-items:center;padding:0 18px;gap:10px;box-shadow:0 3px 5px rgba(0,0,0,.25)}
.account-tab .country{font-style:italic;font-size:15px;color:var(--white);display:flex;align-items:center;gap:8px;padding-right:12px;border-right:1px dashed #777}
.login-btn{margin-left:4px;background:linear-gradient(#2fc6e2,#0f8aa5);color:#0d2a33;font-weight:700;font-size:16px;padding:4px 18px;border-radius:4px;border:1px solid #0b5d70;letter-spacing:.5px}

.brand{position:absolute;left:80px;top:70px;display:flex;align-items:center;gap:12px}
.brand-dot{width:34px;height:34px;border-radius:50%;background:var(--blue)}
.brand-name{font-size:30px;font-weight:600;letter-spacing:4px;color:var(--dark)}

.main-nav a{position:absolute;top:106px;font-size:19px;font-weight:600;color:var(--ink)}
.main-nav .current{left:584px;top:72px;width:90px;height:90px;border-radius:50%;background:radial-gradient(circle at 50% 35%,#3a3a3c,#151516);color:var(--blue);display:flex;align-items:center;justify-content:center;box-shadow:0 2px 4px rgba(0,0,0,.4)}

.slider{position:absolute;left:47px;top:188px;width:1106px;height:357px;border-radius:5px;overflow:hidden;box-shadow:0 10px 14px -6px rgba(0,0,0,.45);background:#000}
.slide-photo{position:absolute;left:0;top:0;width:730px;height:317px;background:radial-gradient(ellipse at 60% 40%,#d9d9d9,#9a9a9a 55%,#3b3b3b)}
.slide-panel{position:absolute;left:730px;top:0;width:376px;height:317px;background:linear-gradient(90deg,#1c1816,#000 40%)}
.slide-copy{position:absolute;right:33px;top:52px;width:300px;text-align:right;color:var(--white);font-size:26px;line-height:31px}
.signup-btn{position:absolute;left:829px;top:228px;width:199px;height:54px;border-radius:4px;background:linear-gradient(#3ac8e2,#0b7a93);border:2px solid #0a5566;color:#0b2a33;font-family:"Oswald",sans-serif;font-size:26px;display:flex;align-items:center;justify-content:center;letter-spacing:1px}
.slider-bar{position:absolute;left:0;top:317px;width:1106px;height:40px;background:linear-gradient(#4a4a4c,#333335);border-top:1px solid #666}
.slider-bar .prev,.slider-bar .next{position:absolute;top:0;height:40px;display:flex;align-items:center;font-family:"Oswald",sans-serif;font-size:22px;color:var(--white);padding:0 10px;background:#2e2e30}
.slider-bar .prev{left:0;width:121px;border-right:1px solid #222}
.slider-bar .next{right:0;width:80px;border-left:1px solid #222}
.dots{position:absolute;left:522px;top:13px;display:flex;gap:6px}
.dots span{width:14px;height:14px;border-radius:50%;background:#1c1c1d;box-shadow:inset 0 1px 2px #000}
.dots .on{background:var(--blue);border:3px solid #1c1c1d}

.feature{position:absolute;top:604px;width:520px}
.feature.left{left:65px}
.feature.right{left:623px}
.feature h2{display:flex;align-items:center;gap:10px;font-size:27px;font-weight:700;color:var(--teal);height:46px}
.feature h2 .badge{width:46px;height:46px;border-radius:50%;background:radial-gradient(circle at 40% 35%,#3a3a3c,#111);color:var(--blue);font-size:30px;display:flex;align-items:center;justify-content:center}
.feature h2 .label{border-bottom:2px solid var(--dark);padding-bottom:2px;padding-right:4px}
.feature p{margin:24px 0 0 17px;width:497px;font-size:17.5px;line-height:24px;text-align:justify}

.site-footer{position:absolute;left:0;top:864px;width:1200px;height:254px;background:var(--panel);border-top:2px solid #bdbdbd;border-bottom:3px solid var(--blue)}
.footer-nav{position:absolute;left:80px;top:52px;list-style:none}
.footer-nav li{font-size:18px;color:var(--white);height:41px}
.footer-nav .current{color:var(--blue)}
.blog-title{position:absolute;left:315px;top:52px;font-size:18px;line-height:24px;color:var(--white)}
.blog-title span{color:var(--blue)}
.blog-card{position:absolute;left:318px;top:90px;width:564px;height:112px;background:var(--panel-deep);border-radius:4px;box-shadow:0 1px 3px rgba(0,0,0,.6);padding:12px 24px}
.blog-card::before{content:"";position:absolute;left:114px;top:-8px;border:8px solid transparent;border-top:0;border-bottom-color:var(--panel-deep)}
.blog-card h3{font-size:19px;font-weight:400;line-height:26px;color:var(--blue);text-decoration:underline}
.blog-card .meta{margin:6px 0 0 12px;font-size:15px;line-height:20px;font-style:italic;color:var(--muted)}
.blog-card .meta a{color:var(--blue)}
.blog-card p{font-size:15px;line-height:17px;color:var(--white)}
.blog-card p a{color:var(--blue);font-style:italic}
.footer-brand{position:absolute;left:930px;top:40px;width:200px;text-align:center;color:var(--white)}
.footer-brand .brand-dot{width:60px;height:60px;margin:0 auto 22px}
.footer-brand .brand-name{color:var(--white);font-size:20px;font-weight:600;letter-spacing:4px}
.footer-brand small{display:block;font-size:16px;margin-top:2px}
</style>
</head>
<body>
<div class="top-strip"></div>

<div class="account-tab">
  <span class="country">
    <svg width="28" height="18" viewBox="0 0 28 18" aria-hidden="true"><rect width="28" height="18" fill="#74acdf"/><rect y="6" width="28" height="6" fill="#fff"/></svg>
    Argentina
  </span>
  <a class="login-btn" href="#">LOGIN</a>
</div>

<a class="brand" href="#"><span class="brand-dot"></span><span class="brand-name">SLOTWISE</span></a>

<nav class="main-nav">
  <a class="current" href="#">HOME</a>
  <a href="#" style="left:735px">FEATURES</a>
  <a href="#" style="left:903px">PRICING</a>
  <a href="#" style="left:1030px">CONTACT</a>
</nav>

<section class="slider">
  <div class="slide-photo" role="img" aria-label="Close-up of a clock face with its minute hand, in soft grey tones"></div>
  <div class="slide-panel"></div>
  <p class="slide-copy">The generated Lorem Ipsum is therefore always free from repetition, injected humour, words etc.</p>
  <a class="signup-btn" href="#">SIGN UP</a>
  <div class="slider-bar">
    <a class="prev" href="#">&lsaquo;PREVIOUS</a>
    <div class="dots"><span class="on"></span><span></span><span></span></div>
    <a class="next" href="#">NEXT&rsaquo;</a>
  </div>
</section>

<section class="feature left">
  <h2><span class="badge">!</span><span class="label">Make yourself available.</span></h2>
  <p>The point of using Lorem Ipsum is that it has a more-or-less normal distribution of letters, as opposed to using 'Content here, content here', making it look like readable English. Many desktop publishing packages and web page editors now use Lorem Ipsum as their.</p>
</section>

<section class="feature right">
  <h2><span class="badge">?</span><span class="label">What’s happening?</span></h2>
  <p>The point of using Lorem Ipsum is that it has a more-or-less normal distribution of letters, as opposed to using 'Content here, content here', making it look like readable English. Many desktop publishing packages and web page editors now use Lorem Ipsum as their.</p>
</section>

<footer class="site-footer">
  <ul class="footer-nav">
    <li class="current">HOME</li>
    <li>FEATURES</li>
    <li>PRICING</li>
    <li>CONTACT US</li>
  </ul>
  <div class="blog-title">FROM THE <span>BLOG</span></div>
  <article class="blog-card">
    <h3>Blog Title Text for a demonstration</h3>
    <div class="meta">by <a href="#">lena.varsou</a> on <a href="#">21/07/2011</a> • <a href="#">3 comments</a></div>
    <p>The point of using Lorem Ipsum is that it has a more-or-less normal distribution of letters, as opposed to using content will... <a href="#">[read more]</a></p>
  </article>
  <div class="footer-brand">
    <div class="brand-dot"></div>
    <div class="brand-name">SLOTWISE</div>
    <small>@2011 Copyright</small>
  </div>
</footer>
</body>
</html>
```